New (old) Business Card Design Project

I would like to purchase a customized version of a design you have previously submitted - https://www.artmarketly.example/design/7305126

I like the card above, and would like to use the same design, jus with my business name, HARLOWAY ASSET ADVISORS. I like the colors in the card above, as well as the font. The other side will have my name, company name, address, phone, email, website, plus disclosure text I will provide.

Target Market(s)

wealthy families

Industry/Entity Type

Financial Services

Contact Information for Business Card

logo on one side, on other my name, company, address, phone, email, website, disclosure language I will provide.

Colors

Designer to choose colors to be used in the design.

Requirements
Must have
• colors: Deep blue and white
Nice to have
• Please see the items I have uploaded, below.
Should not have
• Cheap, tacky look.

```html
<!DOCTYPE html>
<html lang="en">
<head>
<meta charset="utf-8">
<title>Business Card – Harloway Asset Advisors</title>
<link rel="stylesheet" href="https://fonts.googleapis.com/css2?family=Libre+Baskerville:wght@400;700&family=Figtree:wght@400;500;600&family=Playfair+Display:wght@400&display=swap">
<style>
  :root {
    --ink: #2b2b2b;
    --navy: #232c8c;
    --deep-blue-1: #233a70;
    --deep-blue-2: #1f2475;
    --white: #ffffff;
    --page: #ffffff;
    --stage: #e9e9eb;
    --rule: #3a3a3a;
  }
  * { margin: 0; padding: 0; box-sizing: border-box; }
  html, body { width: 1200px; height: 1200px; overflow: hidden; background: var(--page); }
  body { position: relative; font-family: "Figtree", Arial, sans-serif; color: var(--ink); }

  .sheet-header { position: absolute; top: 62px; left: 0; width: 1200px; text-align: center; }
  .sheet-title {
    font-family: "Libre Baskerville", Georgia, serif;
    font-weight: 400; font-size: 46px; color: #333; line-height: 1.1;
  }
  .sheet-spec {
    font-family: "Libre Baskerville", Georgia, serif;
    font-size: 25px; color: var(--navy); margin-top: 4px;
  }

  .stage { position: absolute; top: 216px; left: 0; width: 1200px; height: 984px; background: var(--stage); }

  .card {
    position: absolute; left: 250px; width: 700px; height: 400px;
    box-shadow: 0 6px 18px rgba(0,0,0,0.18);
  }

  /* Contact side */
  .card-back { top: 30px; background: var(--white); }
  .divider { position: absolute; left: 330px; top: 105px; width: 1.5px; height: 265px; background: var(--rule); }
  .identity { position: absolute; right: 390px; top: 110px; text-align: right; }
  .person-name { font-size: 30px; font-weight: 600; color: var(--navy); letter-spacing: 0.2px; }
  .person-title { font-size: 17px; font-weight: 500; margin-top: 4px; letter-spacing: 0.3px; }
  .disclosure-label { position: absolute; right: 390px; top: 330px; font-size: 17px; font-weight: 500; letter-spacing: 0.3px; }

  .contact { position: absolute; left: 355px; top: 110px; width: 330px; font-size: 15px; line-height: 1.35; }
  .contact p { margin-bottom: 11px; }
  .contact .label { font-weight: 600; }
  .contact .web { color: var(--navy); }
  .company-name {
    font-family: "Libre Baskerville", Georgia, serif; font-weight: 700;
    font-size: 13.5px; color: var(--navy); letter-spacing: 0.2px; margin-bottom: 6px !important;
  }
  .disclosure-text { margin-top: 6px; }

  /* Brand side */
  .card-front {
    top: 500px;
    background: linear-gradient(90deg, var(--deep-blue-1), var(--deep-blue-2));
    color: var(--white);
  }
  .brand-name {
    position: absolute; top: 150px; left: 0; width: 100%; text-align: center;
    font-family: "Playfair Display", Georgia, serif; font-weight: 400;
    font-size: 30px; letter-spacing: 5px; color: var(--white);
  }
  .values { position: absolute; top: 285px; left: 100px; right: 80px; display: flex; justify-content: space-between; }
  .value {
    font-family: "Playfair Display", Georgia, serif; font-weight: 400;
    font-size: 20px; letter-spacing: 1px; color: var(--white);
  }
</style>
</head>
<body>
  <header class="sheet-header">
    <h1 class="sheet-title">Business Card - Mockup 1</h1>
    <p class="sheet-spec">Same font &amp; Style as per brief, Size 3.5in X 2.0in, Color : CMYK &amp; RGB</p>
  </header>

  <main class="stage">
    <section class="card card-back" aria-label="Contact side">
      <div class="identity">
        <p class="person-name">DANIEL REYES</p>
        <p class="person-title">MANAGING DIRECTOR</p>
      </div>
      <p class="disclosure-label">DISCLOSURE</p>
      <div class="divider"></div>
      <div class="contact">
        <p><span class="label">Tel:</span> 555-014-7320</p>
        <p><span class="label">Email:</span> team@harlowayaa.example</p>
        <p class="web">www.harlowayaa.example</p>
        <p class="company-name">HARLOWAY ASSET ADVISORS</p>
        <p>18 Linden Court, Suite 204,<br>Westbrook, MA 01900</p>
        <p class="disclosure-text">Lorem ipsum dolor sit amet, consecte tuer adipiscing elit, sed diam onummy nibh</p>
      </div>
    </section>

    <section class="card card-front" aria-label="Brand side">
      <p class="brand-name">HARLOWAY ASSET ADVISORS</p>
      <div class="values">
        <span class="value">Plan</span>
        <span class="value">Preserve</span>
        <span class="value">Prosper</span>
      </div>
    </section>
  </main>
</body>
</html>
```